The Fernway Workshop Business Card

Create a single sided business card using the provided logo.
Use logo 1 in the zip file.

Information on the card:

Marisa Toller B.Ed(Ind Arts)
Partner - Instructor
Phone: (0412) 538 914
Email: marisa@fernwayworkshop.com.au
Website: www.fernwayworkshop.com.au
Facebook: www.socialnook.com/FernwayWorkshopAU
Instagram: www.pictureloop.com/fernway_workshop_au

text colour to be rgb(117,165,22)
background colour (card stock) white.

```html
<!DOCTYPE html>
<html lang="en">
<head>
<meta charset="utf-8">
<title>The Fernway Workshop Business Card</title>
<link rel="stylesheet" href="https://fonts.googleapis.com/css2?family=Montserrat:wght@400;500;700&display=swap">
<style>
  :root {
    --brand-green: rgb(117,165,22);
    --swoosh-green: #9cc43c;
    --emblem-green: #a6cb4a;
    --ink: #222222;
    --card-stock: #ffffff;
    --backdrop: #676765;
  }
  * { margin: 0; padding: 0; box-sizing: border-box; }
  html, body {
    width: 1200px; height: 1200px; overflow: hidden;
    background: var(--backdrop);
    font-family: "Montserrat", Arial, sans-serif;
  }
  .business-card {
    position: absolute; left: 163px; top: 392px;
    width: 876px; height: 526px;
    background: var(--card-stock);
    border-radius: 19px;
    overflow: hidden;
  }
  .brand-name {
    position: absolute; left: 44px; top: 48px;
    width: 440px;
    color: var(--brand-green); font-weight: 700;
    text-transform: uppercase; line-height: 1;
  }
  .brand-main { display: block; font-size: 58px; letter-spacing: -1px; white-space: nowrap; }
  .brand-sub {
    display: flex; align-items: center; gap: 14px;
    margin-top: 6px;
    font-size: 22px; font-weight: 500; letter-spacing: 11px;
  }
  .brand-sub::before, .brand-sub::after {
    content: ""; flex: 1; height: 2px; background: var(--brand-green);
  }
  .name-tab {
    position: absolute; left: 0; top: 172px;
    width: 8px; height: 50px;
    background: var(--brand-green);
    border-radius: 0 4px 4px 0;
  }
  .person-name {
    position: absolute; left: 33px; top: 166px;
    font-size: 33px; font-weight: 700; color: var(--brand-green);
    white-space: nowrap;
  }
  .person-role {
    position: absolute; left: 30px; top: 208px;
    font-size: 19px; font-weight: 400; color: var(--ink);
  }
  .contact-list {
    position: absolute; left: 28px; top: 283px;
    list-style: none;
  }
  .contact-list li {
    display: flex; align-items: center;
    height: 32px;
    font-size: 19px; color: var(--ink); white-space: nowrap;
  }
  .contact-icon {
    width: 18px; height: 18px; margin-right: 12px; flex: none;
    fill: var(--brand-green);
  }
  .emblem {
    position: absolute; left: 503px; top: 126px;
    width: 314px; height: 314px; border-radius: 50%;
    background: var(--emblem-green);
  }
  .card-swoosh {
    position: absolute; left: 0; top: 0; width: 876px; height: 526px;
  }
</style>
</head>
<body>
  <div class="business-card">
    <svg class="card-swoosh" viewBox="0 0 730 438" preserveAspectRatio="none" aria-hidden="true">
      <path d="M0 405 C80 380 200 382 300 392 C420 404 560 430 730 420 L730 438 L0 438 Z" fill="var(--swoosh-green)"/>
      <path d="M385 398 C520 418 660 395 730 348 L730 410 C600 420 480 412 385 398 Z" fill="var(--swoosh-green)"/>
    </svg>

    <div class="brand-name">
      <span class="brand-main">The Fernway</span>
      <span class="brand-sub">Workshop</span>
    </div>

    <div class="name-tab"></div>
    <h1 class="person-name">Marisa Toller B.Ed(Ind Arts)</h1>
    <p class="person-role">Partner - Instructor</p>

    <ul class="contact-list">
      <li>
        <svg class="contact-icon" viewBox="0 0 24 24"><path d="M6.6 10.8a15.1 15.1 0 0 0 6.6 6.6l2.2-2.2a1 1 0 0 1 1-.25 11.4 11.4 0 0 0 3.6.57 1 1 0 0 1 1 1V20a1 1 0 0 1-1 1A17 17 0 0 1 3 4a1 1 0 0 1 1-1h3.5a1 1 0 0 1 1 1c0 1.25.2 2.45.57 3.57a1 1 0 0 1-.25 1z"/></svg>
        (0412) 538 914
      </li>
      <li>
        <svg class="contact-icon" viewBox="0 0 24 24"><path d="M2 5h20v2l-10 6L2 7z"/><path d="M2 9l10 6 10-6v10H2z"/></svg>
        marisa@fernwayworkshop.com.au
      </li>
      <li>
        <svg class="contact-icon" viewBox="0 0 24 24"><circle cx="12" cy="12" r="10"/><path d="M2 12h20M12 2c3 3 3 17 0 20M12 2c-3 3-3 17 0 20" stroke="#fff" stroke-width="1.4" fill="none"/></svg>
        www.fernwayworkshop.com.au
      </li>
      <li>
        <svg class="contact-icon" viewBox="0 0 24 24"><circle cx="12" cy="12" r="10"/></svg>
        www.socialnook.com/FernwayWorkshopAU
      </li>
      <li>
        <svg class="contact-icon" viewBox="0 0 24 24"><circle cx="12" cy="12" r="10"/></svg>
        www.pictureloop.com/fernway_workshop_au
      </li>
    </ul>

    <div class="emblem" role="img" aria-label="Workshop emblem: hammer and tongs crossed above an anvil with a flame, inside a ring"></div>
  </div>
</body>
</html>
```